Wine Bottle Label Graphic Design (mini bottle 187ml)

Looking for a contemporary custom wine label design for party favors. Inspiration photos provided. **Please see "wine favorite" example in uploads.

Artwork 2.5" wide by 2.75" tall to be placed on 3"x3" stickers. Specs from printer attached but I still want image to fit within the artwork size I specified. Please make label center justified. This is for BOYS. It does not need to be super "masculine"...but definitely not feminine.

Required elements:

Colors: white background, include gold and purple to match logo. Other colors are fine to include.

Name: Sababa 13 (I like use of the No) as shown in the sample, but not required
Varietal: Mitzvah Blend 6.11.2021
Vineyard: Hollis Family Vineyard
Location: Maryland
Logo: See attached (KRNotecard Final)

Font styles to use
Serif
Sans Serif

Requirements
Must have
• All the above elements. Clean and crisp design. Contemporary and classy. Purple, Gold, Black colors. See logo. You CAN include cursive font for select elements. I don't mind a combination of print and script.
Should not have
• Floral, scrolling, background image, old fashioned

```html
<!DOCTYPE html>
<html lang="en">
<head>
<meta charset="utf-8">
<title>Sababa No 13 – Label Set</title>
<link href="https://fonts.googleapis.com/css2?family=Libre+Baskerville:wght@400;700&family=Playfair+Display:wght@900&family=Allura&display=swap" rel="stylesheet">
<style>
  :root {
    --canvas: #f3f3f1;
    --label: #ffffff;
    --ink: #2e2e2e;
    --gold: #b8963e;
    --gold-light: #e6d39a;
    --gold-dark: #8a6a22;
    --purple: #6b55a8;
    --black: #151515;
  }
  * { margin: 0; padding: 0; box-sizing: border-box; }
  html, body {
    width: 1200px; height: 1042px; overflow: hidden;
    background: var(--canvas);
  }
  .label-set {
    width: 1200px; height: 1042px;
    display: flex; justify-content: center; align-items: center; gap: 50px;
  }
  .label {
    width: 330px; height: 363px;
    background: var(--label);
    position: relative;
    display: flex; flex-direction: column; align-items: center;
    padding-top: 26px;
    box-shadow: 0 2px 10px rgba(0,0,0,0.08);
  }
  .label::before, .label::after {
    content: ""; position: absolute; left: 0; right: 0; height: 3px;
    background: linear-gradient(90deg, var(--gold-dark), var(--gold-light), var(--gold), var(--gold-light), var(--gold-dark));
  }
  .label::before { top: 10px; }
  .label::after { bottom: 10px; }
  .brand {
    display: flex; align-items: center; gap: 10px;
    font-family: "Libre Baskerville", Georgia, serif;
    font-weight: 700; font-size: 17px; letter-spacing: 0.06em;
    color: var(--purple); text-transform: uppercase;
    height: 56px;
  }
  .brand-dot {
    width: 22px; height: 22px; border-radius: 50%;
    background: var(--purple);
  }
  .wine-name {
    margin-top: 12px;
    font-family: "Libre Baskerville", Georgia, serif;
    font-weight: 700; font-size: 36px; line-height: 44px; color: var(--ink);
    letter-spacing: 0.01em;
  }
  .number {
    margin-top: 10px;
    padding: 3px;
    border: 2px solid var(--ink);
  }
  .number-text {
    display: flex; justify-content: center; align-items: center; gap: 14px;
    width: 172px; height: 42px;
    font-family: "Playfair Display", Georgia, serif;
    font-weight: 900; font-size: 30px; line-height: 1;
    font-variant-numeric: lining-nums;
    letter-spacing: 0.06em;
    color: #fff;
  }
  .number-sign { display: inline-flex; align-items: flex-start; }
  .number-o {
    font-size: 17px; line-height: 1;
    border-bottom: 2px solid currentColor;
    padding-bottom: 1px; margin-left: 2px; margin-top: 1px;
  }
  .number--gold .number-text { background: linear-gradient(90deg, var(--gold-light), var(--gold) 45%, var(--gold-dark)); }
  .number--black .number-text { background: var(--black); }
  .number--purple { border-color: var(--purple); }
  .number--purple .number-text { background: var(--purple); }
  .vineyard {
    margin-top: 14px;
    font-family: "Libre Baskerville", Georgia, serif;
    font-weight: 700; font-size: 16px; line-height: 20px; color: var(--ink);
    letter-spacing: 0.04em; text-transform: uppercase;
  }
  .vineyard-sub {
    margin-top: 3px;
    font-family: "Libre Baskerville", Georgia, serif;
    font-size: 11px; line-height: 14px; color: var(--ink);
    letter-spacing: 0.45em; text-transform: uppercase;
  }
  .varietal {
    margin-top: 5px;
    font-family: "Libre Baskerville", Georgia, serif;
    font-size: 11px; line-height: 14px; color: var(--purple);
    letter-spacing: 0.08em;
  }
  .region {
    margin-top: 2px;
    font-family: "Allura", cursive;
    font-size: 30px; line-height: 34px; color: var(--ink);
  }
</style>
</head>
<body>
<main class="label-set">
  <section class="label">
    <div class="brand"><span class="brand-dot"></span>Kai &amp; Rowan</div>
    <h1 class="wine-name">Sababa</h1>
    <div class="number number--gold"><div class="number-text"><span class="number-sign">N<span class="number-o">o</span></span><span>13</span></div></div>
    <p class="vineyard">Hollis Family</p>
    <p class="vineyard-sub">Vineyard</p>
    <p class="varietal">Mitzvah Blend 6.11.2021</p>
    <p class="region">Maryland</p>
  </section>
  <section class="label">
    <div class="brand"><span class="brand-dot"></span>Kai &amp; Rowan</div>
    <h1 class="wine-name">Sababa</h1>
    <div class="number number--black"><div class="number-text"><span class="number-sign">N<span class="number-o">o</span></span><span>13</span></div></div>
    <p class="vineyard">Hollis Family</p>
    <p class="vineyard-sub">Vineyard</p>
    <p class="varietal">Mitzvah Blend 6.11.2021</p>
    <p class="region">Maryland</p>
  </section>
  <section class="label">
    <div class="brand"><span class="brand-dot"></span>Kai &amp; Rowan</div>
    <h1 class="wine-name">Sababa</h1>
    <div class="number number--purple"><div class="number-text"><span class="number-sign">N<span class="number-o">o</span></span><span>13</span></div></div>
    <p class="vineyard">Hollis Family</p>
    <p class="vineyard-sub">Vineyard</p>
    <p class="varietal">Mitzvah Blend 6.11.2021</p>
    <p class="region">Maryland</p>
  </section>
</main>
</body>
</html>
```